Slide Master for Halvern Engines - A Systematic Hedge Fund

We are looking for someone to produce a theme and slide master for us for our investor presentations. I have uploaded a few examples of templates that we would like to have included:
Main Title
Section Title
Slides with just bullet points
Different image/table configurations with bullet points and foot notes
Biographies of different lengths
A disclaimer (no one will read this but it should still look nice and needs to be in the presentations)
I have also uploaded the company logo, business card and colour definitions. Currently we have a blue colour scheme defined, but it would be nice to get a complementary set of colours so that when we have charts with more elements we can just draw from those.
The most important thing is that the slide master must be of general use to us. We arn't looking to have a specific presentation designed for us, but a theme/style that we can apply ourselves to any presentation we need to give in the future. It should have clearly defined guidelines for where content should go (and if this is different with and without footnotes for example). We would also like it to have a similar feel to the logo/business cards, so matt colours, high contrast, but not busy.
I'm excited to see the results!

```html
<!DOCTYPE html>
<html lang="en">
<head>
<meta charset="utf-8">
<title>Halvern Engines – Slide Master Overview</title>
<link href="https://fonts.googleapis.com/css2?family=Montserrat:wght@400;500;600;700;800&display=swap" rel="stylesheet">
<style>
:root{
  --navy:#16498c;
  --navy-deep:#0f3a73;
  --blue:#4a8fd8;
  --sky:#a8c9ef;
  --grey:#c9ccd1;
  --grey-dark:#8a8f97;
  --ink:#2b2f36;
  --text:#7b8088;
  --canvas:#eceef1;
  --white:#ffffff;
}
*{box-sizing:border-box;margin:0;padding:0}
html,body{width:1200px;height:2981px;overflow:hidden;background:var(--canvas);font-family:"Montserrat",Arial,sans-serif;color:var(--ink)}
.deck{display:grid;grid-template-columns:repeat(3,368px);grid-auto-rows:207px;column-gap:22px;row-gap:20px;padding:26px}
.slide{position:relative;width:368px;height:207px;background:var(--white);overflow:hidden;box-shadow:0 1px 3px rgba(0,0,0,.06)}
.slide.dark{background:var(--navy)}
.abs{position:absolute}
.title{position:absolute;left:12px;top:13px;font-size:11px;font-weight:700;color:var(--navy);letter-spacing:.1px}
.title::before{content:"";position:absolute;left:-12px;top:0;width:2px;height:13px;background:var(--navy)}
.title .accent{color:var(--blue);font-weight:600}
.subtitle{position:absolute;left:12px;top:28px;font-size:4.5px;letter-spacing:1.4px;color:var(--blue);font-weight:600}
.mark{position:absolute;right:10px;top:11px;font-size:5.2px;font-weight:700;color:var(--navy);line-height:1.05;letter-spacing:.8px;text-align:center}
.mark::before{content:"";display:block;width:6px;height:6px;border-radius:50%;background:var(--navy);margin:0 auto 2px}
.foot{position:absolute;left:0;right:0;bottom:0;height:11px;display:flex;justify-content:space-between;align-items:center;padding:0 12px;font-size:3.4px;color:var(--grey-dark);font-weight:600}
.foot::before{content:"";position:absolute;left:0;right:0;top:0;height:1.5px;background:linear-gradient(90deg,var(--navy),var(--sky))}
.p{font-size:3.6px;line-height:5.2px;color:var(--text)}
.h{font-size:4.4px;font-weight:700;color:var(--ink)}
.h.blue{color:var(--blue)}
.h.grey{color:var(--grey-dark)}
.dash{width:8px;height:1px;background:var(--navy);margin:3px 0 5px}
.logo{font-weight:700;color:var(--navy);text-align:center;letter-spacing:2px;line-height:1.05}
.logo.white{color:var(--white)}
.vert{position:absolute;right:9px;top:30px;writing-mode:vertical-rl;font-size:3.6px;letter-spacing:1px;color:var(--grey)}
.dark .vert{color:var(--sky)}
.big-title{font-size:13px;font-weight:700;color:var(--navy);line-height:1.2}
.dark .big-title{color:var(--white)}
.kicker{font-size:4.6px;letter-spacing:1.6px;color:var(--blue);font-weight:600}
.dark .kicker{color:var(--sky)}
.art{position:absolute}
.dot{display:inline-block;width:5px;height:5px;border:.6px solid var(--navy);border-radius:50%;margin-right:1.5px}
.dark .dot{border-color:var(--sky)}
.num{display:flex;align-items:center;justify-content:center;border-radius:50%;color:#fff;font-weight:700}
.photo{position:absolute;background:linear-gradient(135deg,#c9ced6,#8e97a4)}
.bar-label{font-size:3.4px;color:#fff;font-weight:600;display:flex;align-items:center;justify-content:center}
</style>
</head>
<body>
<main class="deck">

<!-- 1 Logo cover -->
<section class="slide">
  <div class="logo abs" style="left:0;right:0;top:78px;font-size:20px">HALVERN<br>ENGINES</div>
  <div class="vert">WWW.HALVERNENGINES.COM</div>
</section>

<!-- 2 Split cover -->
<section class="slide">
  <div class="logo abs" style="left:30px;width:150px;top:86px;font-size:13px">HALVERN<br>ENGINES</div>
  <div class="abs" style="left:186px;top:22px;width:1px;height:163px;background:var(--grey)"></div>
  <div class="abs" style="left:204px;top:36px">
    <div class="big-title">HALVERN<br><span style="color:var(--blue)">ENGINES</span><br>PRESENTATION</div>
    <div class="kicker" style="margin-top:4px">SUBTITLE GOES HERE</div>
    <div class="p" style="margin-top:22px;color:var(--ink)">Month 2021</div>
    <div class="abs" style="top:122px;left:0;border:.8px solid var(--navy);border-radius:8px;padding:2px 8px;font-size:3.6px;font-weight:700;color:var(--navy);letter-spacing:1px;white-space:nowrap">PRESENTER NAME</div>
  </div>
</section>

<!-- 3 Banner cover -->
<section class="slide">
  <div class="logo abs" style="left:0;right:0;top:9px;font-size:6px">HALVERN<br>ENGINES</div>
  <div class="art" role="img" aria-label="Blue network texture background" style="left:0;top:45px;width:368px;height:162px;background:radial-gradient(circle at 70% 30%,#2f6bb5,var(--navy) 55%,var(--navy-deep))"></div>
  <div class="abs" style="left:0;right:0;top:62px;text-align:center;color:#fff">
    <div style="font-size:3.8px;letter-spacing:1.5px;color:var(--sky)">WWW.HALVERNENGINES.COM</div>
    <div style="font-size:13.5px;font-weight:700;margin-top:18px">MASTER SLIDE PRESENTATION</div>
    <div style="font-size:4.6px;letter-spacing:1.8px;margin-top:4px">SUBTITLE GOES HERE</div>
    <div style="font-size:4px;margin-top:15px">Month 2021</div>
    <div style="font-size:3.8px;letter-spacing:1.3px;margin-top:15px;font-weight:600">PRESENTER NAME</div>
  </div>
</section>

<!-- 4 Dark logo -->
<section class="slide dark">
  <div class="logo white abs" style="left:0;right:0;top:78px;font-size:20px">HALVERN<br>ENGINES</div>
  <div class="vert">WWW.HALVERNENGINES.COM</div>
</section>

<!-- 5 Light logo with network -->
<section class="slide">
  <div class="art" role="img" aria-label="Faint grey network of connected nodes" style="inset:0;background:radial-gradient(ellipse at 50% 50%,#fff 30%,#eef0f3 75%,#e4e7eb)"></div>
  <div class="logo abs" style="left:0;right:0;top:80px;font-size:18px;color:var(--ink)">HALVERN<br>ENGINES</div>
  <div class="vert">WWW.HALVERNENGINES.COM</div>
</section>

<!-- 6 Agenda -->
<section class="slide">
  <h2 class="title">Table Of Content/Agenda</h2>
  <div class="mark">HALVERN<br>ENGINES</div>
  <div class="abs" style="left:22px;top:44px;display:grid;grid-template-columns:150px 150px;row-gap:8px;column-gap:20px">
    <div style="display:flex;gap:8px"><span style="font-size:22px;color:var(--grey);font-weight:400;line-height:1">1</span><div><div class="h">Content here</div><div class="p">Get a modern slide that is well designed. Easy to change colours, photos and text.</div></div></div>
    <div style="display:flex;gap:8px"><span style="font-size:22px;color:var(--grey);font-weight:400;line-height:1">4</span><div><div class="h">Content here</div><div class="p">Get a modern slide that is well designed. Easy to change colours, photos and text.</div></div></div>
    <div style="display:flex;gap:8px"><span style="font-size:22px;color:var(--grey);font-weight:400;line-height:1">2</span><div><div class="h">Content here</div><div class="p">Get a modern slide that is well designed. Easy to change colours, photos and text.</div></div></div>
    <div style="display:flex;gap:8px"><span style="font-size:22px;color:var(--grey);font-weight:400;line-height:1">5</span><div><div class="h">Content here</div><div class="p">Get a modern slide that is well designed. Easy to change colours, photos and text.</div></div></div>
    <div style="display:flex;gap:8px"><span style="font-size:22px;color:var(--grey);font-weight:400;line-height:1">3</span><div><div class="h">Content here</div><div class="p">Get a modern slide that is well designed. Easy to change colours, photos and text.</div></div></div>
    <div style="display:flex;gap:8px"><span style="font-size:22px;color:var(--grey);font-weight:400;line-height:1">6</span><div><div class="h">Content here</div><div class="p">Get a modern slide that is well designed. Easy to change colours, photos and text.</div></div></div>
  </div>
  <footer class="foot"><span>HALVERN ENGINES | 2021</span><span>PAGE | 10</span></footer>
</section>

<!-- 7 Title with network, light -->
<section class="slide">
  <div class="art" role="img" aria-label="Line network of connected nodes" style="right:0;top:0;width:190px;height:207px;background:linear-gradient(120deg,rgba(255,255,255,0) 20%,#e5eaf1 60%,#d3dbe6)"></div>
  <div class="logo abs" style="left:26px;top:34px;font-size:8px;text-align:left">HALVERN<br>ENGINES</div>
  <div class="abs" style="left:26px;top:96px">
    <div class="big-title">MASTER SLIDE<br>PRESENTATION</div>
    <div class="kicker" style="margin-top:3px">SUBTITLE GOES HERE</div>
    <div style="margin-top:14px"><span class="dot"></span><span class="dot"></span><span class="dot"></span><span class="dot"></span></div>
  </div>
  <div class="vert">WWW.HALVERNENGINES.COM</div>
</section>

<!-- 8 Title with network, dark -->
<section class="slide dark">
  <div class="art" role="img" aria-label="Line network of connected nodes" style="right:0;top:0;width:200px;height:207px;background:linear-gradient(120deg,rgba(22,73,140,0) 20%,#1d569e 60%,#2763ad)"></div>
  <div class="logo white abs" style="left:26px;top:34px;font-size:8px;text-align:left">HALVERN<br>ENGINES</div>
  <div class="abs" style="left:26px;top:96px">
    <div class="big-title">MASTER SLIDE<br>PRESENTATION</div>
    <div class="kicker" style="margin-top:3px">SUBTITLE GOES HERE</div>
    <div style="margin-top:14px"><span class="dot"></span><span class="dot"></span><span class="dot"></span><span class="dot"></span></div>
  </div>
  <div class="vert">WWW.HALVERNENGINES.COM</div>
</section>

<!-- 9 Introduction -->
<section class="slide">
  <h2 class="title">Introduction</h2>
  <div class="mark">HALVERN<br>ENGINES</div>
  <div class="abs" style="left:38px;top:74px;width:44px;height:44px;border-radius:50%;border:1px solid var(--grey);display:flex;align-items:center;justify-content:center;font-size:30px;font-weight:800;color:var(--blue);line-height:1;padding-top:12px">&rdquo;</div>
  <div class="abs" style="left:118px;top:82px;width:210px">
    <div class="p" style="line-height:6px">You can simply impress your audience and add a unique zing and appeal to your presentations. Easy to change colours, photos and text. Get a modern slide that is well designed. Get a modern slide that is well designed. You can simply impress your audience and add a unique zing and appeal to your presentations.</div>
    <div class="p" style="text-align:right;margin-top:8px;color:var(--ink)">– Name here/ Manager</div>
  </div>
  <footer class="foot"><span>HALVERN ENGINES | 2021</span><span>PAGE | 11</span></footer>
</section>

<!-- 10 Title with frame art right -->
<section class="slide">
  <div class="logo abs" style="left:26px;top:34px;font-size:8px;text-align:left">HALVERN<br>ENGINES</div>
  <div class="abs" style="left:26px;top:96px">
    <div class="big-title">MASTER SLIDE<br>PRESENTATION</div>
    <div class="kicker" style="margin-top:3px">SUBTITLE GOES HERE</div>
  </div>
  <div class="p abs" style="left:30px;top:180px;color:var(--blue)">Month 2021</div>
  <div class="art" role="img" aria-label="Dark blue steel truss bridge illustration" style="left:176px;top:62px;width:192px;height:84px;background:linear-gradient(160deg,var(--navy),#285fa6);clip-path:polygon(0 40%,100% 0,100% 45%,20% 100%,6% 100%)"></div>
</section>

<!-- 11 Title with frame art left -->
<section class="slide">
  <div class="art" role="img" aria-label="Blue node and truss bridge illustration" style="left:0;top:50px;width:175px;height:90px;background:linear-gradient(200deg,var(--navy),var(--sky));clip-path:polygon(0 0,90% 40%,100% 100%,75% 100%,0 55%)"></div>
  <div class="logo abs" style="left:196px;top:34px;font-size:8px;text-align:left">HALVERN<br>ENGINES</div>
  <div class="abs" style="left:196px;top:96px">
    <div class="big-title">MASTER SLIDE<br>PRESENTATION</div>
    <div class="kicker" style="margin-top:3px">SUBTITLE GOES HERE</div>
  </div>
  <div class="p abs" style="left:198px;top:180px;color:var(--blue)">Month 2021</div>
</section>

<!-- 12 Timeline -->
<section class="slide">
  <h2 class="title">Timeline</h2>
  <div class="mark">HALVERN<br>ENGINES</div>
  <svg class="abs" style="left:0;top:0" width="368" height="207" viewBox="0 0 368 207">
    <line x1="18" y1="95" x2="272" y2="95" stroke="#c9ccd1" stroke-width="1"/>
    <g font-family="Montserrat, sans-serif" font-size="3.6" fill="#2b2f36" text-anchor="middle">
      <circle cx="87" cy="95" r="5" fill="#c9ccd1"/><text x="87" y="83">2013</text>
      <circle cx="117" cy="95" r="4" fill="#a8c9ef"/><text x="117" y="108">2014</text>
      <circle cx="153" cy="95" r="5" fill="#a8c9ef"/><text x="153" y="83">2016</text>
      <circle cx="190" cy="95" r="4" fill="#4a8fd8"/><text x="190" y="108">2018</text>
      <circle cx="226" cy="95" r="5" fill="#4a8fd8"/><text x="226" y="83">2019</text>
      <circle cx="258" cy="95" r="4" fill="#16498c"/><text x="258" y="108">2020</text>
      <circle cx="310" cy="95" r="14" fill="#16498c"/><text x="310" y="97" fill="#fff" font-size="6" font-weight="700">2021</text>
      <text x="310" y="76" font-size="8.5" font-weight="600" fill="#16498c">Vision</text>
    </g>
    <text x="22" y="93" font-family="Montserrat, sans-serif" font-size="7" fill="#2b2f36" font-weight="600">Start</text>
    <text x="22" y="101" font-family="Montserrat, sans-serif" font-size="4" fill="#8a8f97">Contents</text>
    <g font-family="Montserrat, sans-serif" font-size="3" fill="#8a8f97" text-anchor="middle">
      <text x="117" y="46">Contents</text><text x="117" y="51">Get a modern slide that</text><text x="117" y="55">is well designed.</text>
      <text x="190" y="46">Contents</text><text x="190" y="51">Get a modern slide that</text><text x="190" y="55">is well designed.</text>
      <text x="258" y="46">Contents</text><text x="258" y="51">Get a modern slide that</text><text x="258" y="55">is well designed.</text>
      <text x="87" y="146">Contents</text><text x="87" y="151">Get a modern slide that</text><text x="87" y="155">is well designed.</text>
      <text x="153" y="146">Contents</text><text x="153" y="151">Get a modern slide that</text><text x="153" y="155">is well designed.</text>
      <text x="226" y="146">Contents</text><text x="226" y="151">Get a modern slide that</text><text x="226" y="155">is well designed.</text>
      <text x="310" y="130">Contents</text><text x="310" y="135">Get a modern slide that</text><text x="310" y="139">is well designed.</text>
    </g>
  </svg>
  <footer class="foot"><span>HALVERN ENGINES | 2021</span><span>PAGE | 12</span></footer>
</section>

<!-- 13 One column -->
<section class="slide">
  <h2 class="title">Your Title Here - One Column</h2>
  <div class="mark">HALVERN<br>ENGINES</div>
  <div class="abs" style="left:28px;top:60px;width:132px">
    <div class="h">Introduction</div><div class="dash"></div>
    <div class="p">You can simply impress your audience and add a unique zing and appeal to your presentations. Easy to change colours, photos and text. Get a modern slide that is well designed. You can simply impress your audience and add a unique zing and appeal to your presentations. Easy to change colours, photos and text. Get a modern slide that is well designed.</div>
  </div>
  <div class="logo abs" style="left:190px;top:86px;width:150px;font-size:13px;color:#e4e7eb">HALVERN<br>ENGINES</div>
  <footer class="foot"><span>HALVERN ENGINES | 2021</span><span>PAGE | 13</span></footer>
</section>

<!-- 14 Two column -->
<section class="slide">
  <h2 class="title">Your Title Here - Two Column</h2>
  <div class="mark">HALVERN<br>ENGINES</div>
  <div class="abs" style="left:28px;top:60px;width:130px">
    <div class="h">Content Here</div><div class="dash"></div>
    <div class="p">You can simply impress your audience and add a unique zing and appeal to your presentations. Easy to change colours, photos and text. Get a modern slide that is well designed. You can simply impress your audience and add a unique zing and appeal to your presentations. Easy to change colours.</div>
  </div>
  <div class="abs" style="left:204px;top:60px;width:130px">
    <div class="h blue">Content Here</div><div class="dash" style="background:var(--blue)"></div>
    <div class="p">You can simply impress your audience and add a unique zing and appeal to your presentations. Easy to change colours, photos and text. Get a modern slide that is well designed. You can simply impress your audience and add a unique zing and appeal to your presentations. Easy to change colours.</div>
  </div>
  <footer class="foot"><span>HALVERN ENGINES | 2021</span><span>PAGE | 14</span></footer>
</section>

<!-- 15 Three column -->
<section class="slide">
  <h2 class="title">Your Title Here - Three Column</h2>
  <div class="mark">HALVERN<br>ENGINES</div>
  <div class="abs" style="left:22px;top:60px;width:90px">
    <div class="h">Content Here</div><div class="dash"></div>
    <div class="p">You can simply impress your audience and add a unique zing and appeal to your presentations. Easy to change colours, photos and text. Get a modern slide that is well designed. You can simply impress your audience and add a unique zing.</div>
  </div>
  <div class="abs" style="left:134px;top:60px;width:90px">
    <div class="h blue">Content Here</div><div class="dash" style="background:var(--blue)"></div>
    <div class="p">You can simply impress your audience and add a unique zing and appeal to your presentations. Easy to change colours, photos and text. Get a modern slide that is well designed. You can simply impress your audience and add a unique zing.</div>
  </div>
  <div class="abs" style="left:246px;top:60px;width:90px">
    <div class="h grey">Content Here</div><div class="dash" style="background:var(--grey)"></div>
    <div class="p">You can simply impress your audience and add a unique zing and appeal to your presentations. Easy to change colours, photos and text. Get a modern slide that is well designed. You can simply impress your audience and add a unique zing.</div>
  </div>
  <footer class="foot"><span>HALVERN ENGINES | 2021</span><span>PAGE | 15</span></footer>
</section>

<!-- 16 Foot notes, chart right -->
<section class="slide">
  <h2 class="title">Your Title Here <span class="accent">- with foot notes<sup style="font-size:5px">1</sup></span></h2>
  <div class="subtitle">SUBTITLE GOES HERE</div>
  <div class="mark">HALVERN<br>ENGINES</div>
  <div class="abs" style="left:26px;top:58px;width:128px">
    <div style="display:flex;gap:4px"><span class="num" style="width:6px;height:6px;background:var(--navy);font-size:4px;flex:none">✓</span><div class="p">You can simply impress your audience and add a unique zing and appeal to your presentations. Easy to change colours, photos and text. Get a modern slide that is well designed.</div></div>
    <div style="display:flex;gap:4px;margin-top:14px"><span class="num" style="width:6px;height:6px;background:var(--blue);font-size:4px;flex:none">✓</span><div class="p">You can simply impress your audience and add a unique zing and appeal to your presentations. Easy to change colours, photos and text. Get a modern slide that is well designed.</div></div>
  </div>
  <svg class="abs" style="left:164px;top:58px" width="180" height="96" viewBox="0 0 180 96">
    <g stroke="#e4e7eb" stroke-width=".5"><line x1="12" y1="8" x2="176" y2="8"/><line x1="12" y1="24" x2="176" y2="24"/><line x1="12" y1="40" x2="176" y2="40"/><line x1="12" y1="56" x2="176" y2="56"/><line x1="12" y1="72" x2="176" y2="72"/><line x1="12" y1="88" x2="176" y2="88"/></g>
    <polyline fill="none" stroke="#16498c" stroke-width="1" points="14,86 24,82 32,78 40,80 50,70 58,66 66,68 76,58 86,52 94,54 104,44 112,38 122,40 130,32 140,28 148,30 158,22 168,18 176,16"/>
    <g font-family="Montserrat, sans-serif" font-size="3" fill="#8a8f97"><text x="0" y="9">$24M</text><text x="0" y="41">$16M</text><text x="0" y="73">$8M</text><text x="20" y="95">2010</text><text x="62" y="95">2012</text><text x="104" y="95">2014</text><text x="146" y="95">2016</text></g>
  </svg>
  <div class="abs" style="left:12px;right:12px;top:176px;border-top:.5px solid var(--grey);padding-top:2px;font-size:2.8px;color:var(--text);line-height:3.6px"><b>Add foot notes:</b> You can simply impress your audience and add a unique zing and appeal to your presentations. Easy to change colours, photos and text. Get a modern slide that is well designed.</div>
  <footer class="foot"><span>HALVERN ENGINES | 2021</span><span>PAGE | 16</span></footer>
</section>

<!-- 17 Foot notes, chart left -->
<section class="slide">
  <h2 class="title">Your Title Here <span class="accent">- with foot notes<sup style="font-size:5px">2</sup></span></h2>
  <div class="subtitle">SUBTITLE GOES HERE</div>
  <div class="mark">HALVERN<br>ENGINES</div>
  <svg class="abs" style="left:20px;top:58px" width="150" height="96" viewBox="0 0 150 96">
    <g stroke="#e4e7eb" stroke-width=".5"><line x1="12" y1="8" x2="148" y2="8"/><line x1="12" y1="24" x2="148" y2="24"/><line x1="12" y1="40" x2="148" y2="40"/><line x1="12" y1="56" x2="148" y2="56"/><line x1="12" y1="72" x2="148" y2="72"/><line x1="12" y1="88" x2="148" y2="88"/></g>
    <polyline fill="none" stroke="#16498c" stroke-width="1" points="14,86 22,82 30,78 38,80 46,70 54,66 62,68 70,58 78,52 86,54 94,44 102,38 110,40 118,32 126,28 134,30 140,22 148,18"/>
    <g font-family="Montserrat, sans-serif" font-size="3" fill="#8a8f97"><text x="0" y="9">$24M</text><text x="0" y="41">$16M</text><text x="0" y="73">$8M</text><text x="18" y="95">2010</text><text x="54" y="95">2012</text><text x="90" y="95">2014</text><text x="126" y="95">2016</text></g>
  </svg>
  <div class="abs" style="left:196px;top:64px;width:136px">
    <div style="display:flex;gap:4px"><span class="num" style="width:6px;height:6px;background:var(--navy);font-size:4px;flex:none">✓</span><div class="p">You can simply impress your audience and add a unique zing and appeal to your presentations. Easy to change colours, photos and text.</div></div>
    <div style="display:flex;gap:4px;margin-top:18px"><span class="num" style="width:6px;height:6px;background:var(--blue);font-size:4px;flex:none">✓</span><div class="p">You can simply impress your audience and add a unique zing and appeal to your presentations. Easy to change colours, photos and text.</div></div>
  </div>
  <div class="abs" style="left:12px;right:12px;top:176px;border-top:.5px solid var(--grey);padding-top:2px;font-size:2.8px;color:var(--text);line-height:3.6px"><b>Add foot notes:</b> You can simply impress your audience and add a unique zing and appeal to your presentations. Easy to change colours, photos and text. Get a modern slide that is well designed.</div>
  <footer class="foot"><span>HALVERN ENGINES | 2021</span><span>PAGE | 17</span></footer>
</section>

<!-- 18 Bullet points -->
<section class="slide">
  <h2 class="title">Bullets Points</h2>
  <div class="mark">HALVERN<br>ENGINES</div>
  <div class="abs" style="left:30px;top:56px;display:grid;grid-template-columns:150px 150px;row-gap:12px;column-gap:16px">
    <div style="display:flex;gap:8px"><span class="num" style="width:16px;height:16px;background:var(--navy);font-size:6px;flex:none">1</span><div><div class="h">Content Title here</div><div class="p">Get a clean &amp; modern slide that is well designed. Easy to change colours, photos and text.</div></div></div>
    <div style="display:flex;gap:8px"><span class="num" style="width:16px;height:16px;background:var(--navy);font-size:6px;flex:none">4</span><div><div class="h">Content Title here</div><div class="p">Get a clean &amp; modern slide that is well designed. Easy to change colours, photos and text.</div></div></div>
    <div style="display:flex;gap:8px"><span class="num" style="width:16px;height:16px;background:var(--blue);font-size:6px;flex:none">2</span><div><div class="h blue">Content Title here</div><div class="p">Get a clean &amp; modern slide that is well designed. Easy to change colours, photos and text.</div></div></div>
    <div style="display:flex;gap:8px"><span class="num" style="width:16px;height:16px;background:var(--blue);font-size:6px;flex:none">5</span><div><div class="h blue">Content Title here</div><div class="p">Get a clean &amp; modern slide that is well designed. Easy to change colours, photos and text.</div></div></div>
    <div style="display:flex;gap:8px"><span class="num" style="width:16px;height:16px;background:var(--grey);font-size:6px;flex:none">3</span><div><div class="h">Content Title here</div><div class="p">Get a clean &amp; modern slide that is well designed. Easy to change colours, photos and text.</div></div></div>
    <div style="display:flex;gap:8px"><span class="num" style="width:16px;height:16px;background:var(--grey);font-size:6px;flex:none">6</span><div><div class="h">Content Title here</div><div class="p">Get a clean &amp; modern slide that is well designed. Easy to change colours, photos and text.</div></div></div>
  </div>
  <footer class="foot"><span>HALVERN ENGINES | 2021</span><span>PAGE | 18</span></footer>
</section>

<!-- 19 Text with image -->
<section class="slide">
  <h2 class="title">Your Title Here</h2>
  <div class="subtitle">SUBTITLE GOES HERE</div>
  <div class="mark">HALVERN<br>ENGINES</div>
  <div class="abs" style="left:28px;top:60px;width:130px">
    <div class="h">Content Here</div><div class="dash"></div>
    <div class="p">You can simply impress your audience and add a unique zing and appeal to your presentations. Easy to change colours, photos and text. Get a modern slide that is well designed. You can simply impress your audience and add a unique zing and appeal to your presentations. Easy to change colours.</div>
  </div>
  <div class="photo" role="img" aria-label="Photo of a laptop with code on a bright desk" style="left:204px;top:60px;width:134px;height:96px;border-radius:6px;background:linear-gradient(135deg,#f2f4f7,#c5ccd6 60%,#5d6673)"></div>
  <div class="num abs" style="left:172px;top:70px;width:16px;height:16px;background:var(--navy);font-size:6px">▤</div>
  <div class="num abs" style="left:172px;top:92px;width:16px;height:16px;background:var(--blue);font-size:6px">▣</div>
  <div class="num abs" style="left:172px;top:114px;width:16px;height:16px;background:var(--grey);font-size:6px">✎</div>
  <footer class="foot"><span>HALVERN ENGINES | 2021</span><span>PAGE | 19</span></footer>
</section>

<!-- 20 CEO -->
<section class="slide">
  <h2 class="title">CEO DIRECTOR</h2>
  <div class="subtitle">HALVERN ENGINES PRESENTATION</div>
  <div class="mark">HALVERN<br>ENGINES</div>
  <div class="photo" role="img" aria-label="Portrait photo of the director in a suit" style="left:44px;top:56px;width:70px;height:70px;background:linear-gradient(160deg,#dfe3e8,#6d7480)"></div>
  <div class="h abs" style="left:44px;top:134px;width:70px;text-align:center">NAME HERE</div>
  <div class="abs" style="left:56px;top:160px"><span class="dot"></span><span class="dot"></span><span class="dot"></span><span class="dot"></span></div>
  <div class="abs" style="left:132px;top:58px;width:70px"><div class="h">Content Here</div><div class="p" style="margin-top:3px">Get a modern slide that is well designed. Get a modern slide that is clean.</div><div class="p" style="border:.5px solid var(--grey);border-radius:4px;display:inline-block;padding:0 4px;margin-top:4px">LEARN MORE</div></div>
  <div class="abs" style="left:218px;top:58px;width:70px"><div class="h blue">Content Here</div><div class="p" style="margin-top:3px">Get a modern slide that is well designed. Get a modern slide that is clean.</div><div class="p" style="border:.5px solid var(--grey);border-radius:4px;display:inline-block;padding:0 4px;margin-top:4px">LEARN MORE</div></div>
  <div class="abs" style="left:132px;top:120px;width:208px">
    <div style="height:6px;background:#e4e7eb;position:relative"><div class="bar-label" style="position:absolute;left:0;top:0;height:6px;width:90%;background:var(--navy);justify-content:flex-start;padding-left:3px">Content Title</div><span class="p abs" style="right:-1px;top:-5px;color:var(--ink)">90%</span></div>
    <div style="height:6px;background:#e4e7eb;position:relative;margin-top:6px"><div class="bar-label" style="position:absolute;left:0;top:0;height:6px;width:75%;background:var(--blue);justify-content:flex-start;padding-left:3px">Content Title</div><span class="p abs" style="right:-1px;top:-5px;color:var(--ink)">75%</span></div>
  </div>
  <div class="p abs" style="right:30px;top:164px">name@youremailaddress.com</div>
  <footer class="foot"><span>HALVERN ENGINES | 2021</span><span>PAGE | 20</span></footer>
</section>

<!-- 21 Team -->
<section class="slide">
  <h2 class="title">Our Team</h2>
  <div class="mark">HALVERN<br>ENGINES</div>
  <div class="abs" style="left:30px;top:48px;display:grid;grid-template-columns:repeat(4,68px);column-gap:10px">
    <div><div role="img" aria-label="Team member portrait photo" style="height:58px;background:linear-gradient(160deg,#e3d8cf,#8c7a6c)"></div><div class="bar-label" style="height:8px;background:var(--navy);font-size:4px">Member Name</div><div class="p" style="text-align:center;letter-spacing:1px;color:var(--blue);margin-top:2px">POSITION</div><div class="p" style="text-align:center">Get a modern slide that is well designed.</div><div style="text-align:center;margin-top:3px"><span class="dot"></span><span class="dot"></span><span class="dot"></span><span class="dot"></span></div></div>
    <div><div role="img" aria-label="Team member portrait photo" style="height:58px;background:linear-gradient(160deg,#e6d3d3,#9a5a5c)"></div><div class="bar-label" style="height:8px;background:var(--blue);font-size:4px">Member Name</div><div class="p" style="text-align:center;letter-spacing:1px;color:var(--blue);margin-top:2px">POSITION</div><div class="p" style="text-align:center">Get a modern slide that is well designed.</div><div style="text-align:center;margin-top:3px"><span class="dot"></span><span class="dot"></span><span class="dot"></span><span class="dot"></span></div></div>
    <div><div role="img" aria-label="Team member portrait photo" style="height:58px;background:linear-gradient(160deg,#e9e9e9,#6f645c)"></div><div class="bar-label" style="height:8px;background:var(--grey-dark);font-size:4px">Member Name</div><div class="p" style="text-align:center;letter-spacing:1px;color:var(--blue);margin-top:2px">POSITION</div><div class="p" style="text-align:center">Get a modern slide that is well designed.</div><div style="text-align:center;margin-top:3px"><span class="dot"></span><span class="dot"></span><span class="dot"></span><span class="dot"></span></div></div>
    <div><div role="img" aria-label="Team member portrait photo" style="height:58px;background:linear-gradient(160deg,#d9dce0,#4b4743)"></div><div class="bar-label" style="height:8px;background:var(--sky);font-size:4px">Member Name</div><div class="p" style="text-align:center;letter-spacing:1px;color:var(--blue);margin-top:2px">POSITION</div><div class="p" style="text-align:center">Get a modern slide that is well designed.</div><div style="text-align:center;margin-top:3px"><span class="dot"></span><span class="dot"></span><span class="dot"></span><span class="dot"></span></div></div>
  </div>
  <footer class="foot"><span>HALVERN ENGINES | 2021</span><span>PAGE | 21</span></footer>
</section>

<!-- 22 Four cards -->
<section class="slide">
  <h2 class="title">Your Title Here</h2>
  <div class="subtitle">SUBTITLE GOES HERE</div>
  <div class="mark">HALVERN<br>ENGINES</div>
  <div class="abs" style="left:36px;top:50px;display:grid;grid-template-columns:repeat(4,68px);column-gap:7px">
    <div style="border:.6px solid var(--grey);height:108px;position:relative;padding:6px"><div style="font-size:12px;font-weight:700;color:var(--ink)">01</div><div class="p" style="margin-top:4px">Lorem ipsum is simply dummy text of the printing and typesetting trade since the 1500s.</div><div class="bar-label abs" style="left:0;right:0;bottom:0;height:8px;background:var(--navy);font-size:4px">Option Name</div></div>
    <div style="border:.6px solid var(--grey);height:108px;position:relative;padding:6px"><div style="font-size:12px;font-weight:700;color:var(--blue)">02</div><div class="p" style="margin-top:4px">Lorem ipsum is simply dummy text of the printing and typesetting trade since the 1500s.</div><div class="bar-label abs" style="left:0;right:0;bottom:0;height:8px;background:var(--blue);font-size:4px">Option Name</div></div>
    <div style="border:.6px solid var(--grey);height:108px;position:relative;padding:6px"><div style="font-size:12px;font-weight:700;color:var(--sky)">03</div><div class="p" style="margin-top:4px">Lorem ipsum is simply dummy text of the printing and typesetting trade since the 1500s.</div><div class="bar-label abs" style="left:0;right:0;bottom:0;height:8px;background:var(--grey-dark);font-size:4px">Option Name</div></div>
    <div style="border:.6px solid var(--grey);height:108px;position:relative;padding:6px"><div style="font-size:12px;font-weight:700;color:var(--ink)">04</div><div class="p" style="margin-top:4px">Lorem ipsum is simply dummy text of the printing and typesetting trade since the 1500s.</div><div class="bar-label abs" style="left:0;right:0;bottom:0;height:8px;background:#e4e7eb;color:var(--grey-dark);font-size:4px">Option Name</div></div>
  </div>
  <footer class="foot"><span>HALVERN ENGINES | 2021</span><span>PAGE | 22</span></footer>
</section>

<!-- 23 Infographic -->
<section class="slide">
  <h2 class="title">Your Title Here - Infographic</h2>
  <div class="mark">HALVERN<br>ENGINES</div>
  <svg class="abs" style="left:40px;top:40px" width="120" height="130" viewBox="0 0 120 130">
    <circle cx="40" cy="70" r="36" fill="none" stroke="#c9ccd1" stroke-width=".6" stroke-dasharray="2 2"/>
    <circle cx="40" cy="70" r="20" fill="#fff" stroke="#e4e7eb"/>
    <circle cx="66" cy="28" r="9" fill="#16498c"/><circle cx="88" cy="55" r="9" fill="#4a8fd8"/><circle cx="88" cy="85" r="9" fill="#8a8f97"/><circle cx="66" cy="112" r="9" fill="#a8c9ef"/>
  </svg>
  <div class="abs" style="left:58px;top:104px;width:44px;font-size:4.4px;font-weight:700;color:var(--navy);text-align:center;line-height:1.1">HALVERN<br>ENGINES</div>
  <div class="abs" style="left:190px;top:48px;width:150px;display:grid;row-gap:9px">
    <div style="display:flex;gap:5px"><span class="num" style="width:6px;height:6px;background:var(--navy);font-size:4px;flex:none">✓</span><div><div class="h">Content Title</div><div class="p">Get a clean &amp; modern slide that is well designed.</div></div></div>
    <div style="display:flex;gap:5px"><span class="num" style="width:6px;height:6px;background:var(--blue);font-size:4px;flex:none">✓</span><div><div class="h blue">Content Title</div><div class="p">Get a clean &amp; modern slide that is well designed.</div></div></div>
    <div style="display:flex;gap:5px"><span class="num" style="width:6px;height:6px;background:var(--grey-dark);font-size:4px;flex:none">✓</span><div><div class="h">Content Title</div><div class="p">Get a clean &amp; modern slide that is well designed.</div></div></div>
    <div style="display:flex;gap:5px"><span class="num" style="width:6px;height:6px;background:var(--sky);font-size:4px;flex:none">✕</span><div><div class="h">Content Title</div><div class="p">Get a clean &amp; modern slide that is well designed.</div></div></div>
  </div>
  <footer class="foot"><span>HALVERN ENGINES | 2021</span><span>PAGE | 23</span></footer>
</section>

<!-- 24 Pie charts -->
<section class="slide">
  <h2 class="title">Pie Charts</h2>
  <div class="mark">HALVERN<br>ENGINES</div>
  <div class="p abs" style="left:50px;right:50px;top:46px;text-align:center">Get a clean &amp; modern slide that is well designed. Easy to change colours, photos and text. You can simply impress your audience and add a unique zing and appeal.</div>
  <svg class="abs" style="left:30px;top:70px" width="310" height="80" viewBox="0 0 310 80" font-family="Montserrat, sans-serif">
    <g transform="translate(55,38)"><circle r="20" fill="none" stroke="#e4e7eb" stroke-width="5"/><circle r="20" fill="none" stroke="#16498c" stroke-width="5" stroke-dasharray="85.4 125.7" transform="rotate(-90)"/><text y="3.5" text-anchor="middle" font-size="10" font-weight="600" fill="#2b2f36">68%</text></g>
    <g transform="translate(155,38)"><circle r="20" fill="none" stroke="#e4e7eb" stroke-width="5"/><circle r="20" fill="none" stroke="#4a8fd8" stroke-width="5" stroke-dasharray="44 125.7" transform="rotate(-90)"/><text y="3.5" text-anchor="middle" font-size="10" font-weight="600" fill="#4a8fd8">35%</text></g>
    <g transform="translate(255,38)"><circle r="20" fill="none" stroke="#e4e7eb" stroke-width="5"/><circle r="20" fill="none" stroke="#8a8f97" stroke-width="5" stroke-dasharray="69.1 125.7" transform="rotate(-90)"/><text y="3.5" text-anchor="middle" font-size="10" font-weight="600" fill="#8a8f97">55%</text></g>
  </svg>
  <div class="p abs" style="left:60px;top:152px;width:50px;text-align:center">Get a clean &amp; modern slide that is well designed</div>
  <div class="p abs" style="left:160px;top:152px;width:50px;text-align:center">Get a clean &amp; modern slide that is well designed</div>
  <div class="p abs" style="left:260px;top:152px;width:50px;text-align:center">Get a clean &amp; modern slide that is well designed</div>
  <footer class="foot"><span>HALVERN ENGINES | 2021</span><span>PAGE | 24</span></footer>
</section>

<!-- 25 Infographic numbers -->
<section class="slide">
  <h2 class="title">Infographic Style</h2>
  <div class="mark">HALVERN<br>ENGINES</div>
  <div class="abs" style="left:18px;top:42px;width:146px;height:120px;box-shadow:0 1px 6px rgba(0,0,0,.12);background:#fff">
    <div class="num abs" style="left:28px;top:16px;width:12px;height:12px;background:var(--navy);font-size:7px">$</div>
    <div class="abs" style="left:34px;top:18px;font-size:40px;font-weight:800;color:var(--navy);line-height:1">08</div>
    <div class="bar-label abs" style="left:106px;top:54px;width:24px;height:8px;background:var(--navy);font-size:3.6px">COST</div>
    <div class="abs" style="left:0;right:0;top:72px;text-align:center;font-size:9px;font-weight:700;color:var(--navy)">Million</div>
    <div class="p abs" style="left:20px;right:20px;top:88px;text-align:center">Get a modern slide that is well designed.</div>
  </div>
  <div class="num abs" style="left:178px;top:44px;width:11px;height:11px;background:var(--sky);font-size:6px">$</div>
  <div class="abs" style="left:184px;top:46px;font-size:30px;font-weight:800;color:var(--blue);line-height:1">04</div>
  <div class="bar-label abs" style="left:240px;top:56px;width:22px;height:7px;background:var(--blue);font-size:3.4px">SALES</div>
  <div class="abs" style="left:240px;top:65px;font-size:7px;font-weight:600;color:var(--blue)">Million</div>
  <div class="p abs" style="left:278px;top:52px;width:48px">Get a modern slide that is well designed.</div>
  <div class="num abs" style="left:226px;top:100px;width:10px;height:10px;background:#e4e7eb;color:var(--grey-dark);font-size:5px">%</div>
  <div class="abs" style="left:184px;top:108px;font-size:30px;font-weight:800;color:var(--grey);line-height:1">15</div>
  <div class="bar-label abs" style="left:238px;top:122px;width:38px;height:7px;background:var(--grey);font-size:3.4px">PERCENTAGE</div>
  <div class="p abs" style="left:282px;top:116px;width:44px">Get a modern slide that is well designed.</div>
  <footer class="foot"><span>HALVERN ENGINES | 2021</span><span>PAGE | 25</span></footer>
</section>

<!-- 26 Section 01 -->
<section class="slide dark">
  <div class="art" role="img" aria-label="Faint blue network texture" style="inset:0;background:linear-gradient(135deg,var(--navy),#1b528f 60%,var(--navy-deep))"></div>
  <div class="logo white abs" style="left:184px;right:0;top:34px;font-size:11px">HALVERN<br>ENGINES</div>
  <div class="abs" style="left:26px;top:142px;font-size:32px;font-weight:700;color:#fff;line-height:1">01</div>
  <div class="abs" style="left:72px;top:144px;width:1px;height:32px;background:var(--sky)"></div>
  <div class="abs" style="left:82px;top:146px">
    <div style="font-size:11px;font-weight:700;color:#fff">SECTION TITLE</div>
    <div class="p" style="color:var(--sky);margin-top:4px">Get a modern slide that is well designed. Easy to change colours, photos and text.</div>
  </div>
</section>

<!-- 27 Section 02 -->
<section class="slide">
  <div class="art" role="img" aria-label="Faint grey network of connected nodes" style="inset:0;background:radial-gradient(ellipse at 40% 40%,#fff 30%,#eef0f3 80%)"></div>
  <div class="logo abs" style="left:184px;right:0;top:34px;font-size:11px;color:var(--ink)">HALVERN<br>ENGINES</div>
  <div class="abs" style="left:26px;top:142px;font-size:32px;font-weight:700;color:var(--ink);line-height:1">02</div>
  <div class="abs" style="left:72px;top:144px;width:1px;height:32px;background:var(--grey)"></div>
  <div class="abs" style="left:82px;top:146px">
    <div style="font-size:11px;font-weight:700;color:var(--ink)">SECTION TITLE</div>
    <div class="p" style="margin-top:4px">Get a modern slide that is well designed. Easy to change colours, photos and text.</div>
  </div>
</section>

<!-- 28 Ring infographic -->
<section class="slide">
  <h2 class="title">Infographic Style</h2>
  <div class="mark">HALVERN<br>ENGINES</div>
  <svg class="abs" style="left:134px;top:46px" width="100" height="100" viewBox="-50 -50 100 100">
    <g fill="none" stroke-width="18">
      <circle r="36" stroke="#16498c" stroke-dasharray="27 199.2" transform="rotate(-90)"/>
      <circle r="36" stroke="#4a8fd8" stroke-dasharray="27 199.2" transform="rotate(-45)"/>
      <circle r="36" stroke="#a8c9ef" stroke-dasharray="27 199.2" transform="rotate(0)"/>
      <circle r="36" stroke="#16498c" stroke-dasharray="27 199.2" transform="rotate(45)"/>
      <circle r="36" stroke="#4a8fd8" stroke-dasharray="27 199.2" transform="rotate(90)"/>
      <circle r="36" stroke="#a8c9ef" stroke-dasharray="27 199.2" transform="rotate(135)"/>
      <circle r="36" stroke="#16498c" stroke-dasharray="27 199.2" transform="rotate(180)"/>
      <circle r="36" stroke="#4a8fd8" stroke-dasharray="27 199.2" transform="rotate(225)"/>
    </g>
  </svg>
  <div class="abs" style="left:18px;top:50px;width:110px;text-align:right;display:grid;row-gap:8px">
    <div><div class="h">Content Title</div><div class="p">Get a clean &amp; modern slide that is well designed.</div></div>
    <div><div class="h blue">Content Title</div><div class="p">Get a clean &amp; modern slide that is well designed.</div></div>
    <div><div class="h" style="color:var(--sky)">Content Title</div><div class="p">Get a clean &amp; modern slide that is well designed.</div></div>
    <div><div class="h">Content Title</div><div class="p">Get a clean &amp; modern slide that is well designed.</div></div>
  </div>
  <div class="abs" style="left:244px;top:50px;width:110px;display:grid;row-gap:8px">
    <div><div class="h">Content Title</div><div class="p">Get a clean &amp; modern slide that is well designed.</div></div>
    <div><div class="h blue">Content Title</div><div class="p">Get a clean &amp; modern slide that is well designed.</div></div>
    <div><div class="h" style="color:var(--sky)">Content Title</div><div class="p">Get a clean &amp; modern slide that is well designed.</div></div>
    <div><div class="h">Content Title</div><div class="p">Get a clean &amp; modern slide that is well designed.</div></div>
  </div>
  <footer class="foot"><span>HALVERN ENGINES | 2021</span><span>PAGE | 28</span></footer>
</section>

<!-- 29 SWOT -->
<section class="slide">
  <h2 class="title">SWOT Analysis</h2>
  <div class="mark">HALVERN<br>ENGINES</div>
  <svg class="abs" style="left:134px;top:54px" width="100" height="100" viewBox="0 0 100 100" font-family="Montserrat, sans-serif" font-weight="700" font-size="9" text-anchor="middle">
    <circle cx="50" cy="24" r="20" fill="#16498c"/><circle cx="50" cy="24" r="9" fill="#fff"/><text x="50" y="27" fill="#16498c">S</text>
    <circle cx="76" cy="50" r="20" fill="#4a8fd8"/><circle cx="76" cy="50" r="9" fill="#fff"/><text x="76" y="53" fill="#4a8fd8">W</text>
    <circle cx="24" cy="50" r="20" fill="#a8c9ef"/><circle cx="24" cy="50" r="9" fill="#fff"/><text x="24" y="53" fill="#a8c9ef">T</text>
    <circle cx="50" cy="76" r="20" fill="#e4e7eb"/><circle cx="50" cy="76" r="9" fill="#fff"/><text x="50" y="79" fill="#8a8f97">O</text>
  </svg>
  <div class="abs" style="left:20px;top:66px;width:104px;text-align:right"><div class="h">Strength</div><div class="p">Lorem ipsum dolor sit amet, consectetuer adipiscing elit, sed diam nonummy nibh euismod.</div></div>
  <div class="abs" style="left:244px;top:62px;width:104px"><div class="h blue">Weakness</div><div class="p">Lorem ipsum dolor sit amet, consectetuer adipiscing elit, sed diam nonummy nibh euismod.</div></div>
  <div class="abs" style="left:20px;top:132px;width:104px;text-align:right"><div class="h" style="color:var(--sky)">Threat</div><div class="p">Lorem ipsum dolor sit amet, consectetuer adipiscing elit, sed diam nonummy nibh euismod.</div></div>
  <div class="abs" style="left:244px;top:136px;width:104px"><div class="h">Opportunity</div><div class="p">Lorem ipsum dolor sit amet, consectetuer adipiscing elit, sed diam nonummy nibh euismod.</div></div>
  <footer class="foot"><span>HALVERN ENGINES | 2021</span><span>PAGE | 29</span></footer>
</section>

<!-- 30 Bar chart -->
<section class="slide">
  <h2 class="title">Bar Chart</h2>
  <div class="subtitle">SUBTITLE GOES HERE</div>
  <div class="mark">HALVERN<br>ENGINES</div>
  <div class="p abs" style="left:80px;right:80px;top:38px;text-align:center">Lorem ipsum dolor sit amet, consectetur adipiscing elit. In ut tortor in urna aucto blandit.</div>
  <svg class="abs" style="left:14px;top:54px" width="344" height="110" viewBox="0 0 344 110" font-family="Montserrat, sans-serif" font-size="3.4">
    <g stroke="#e4e7eb" stroke-width=".5"><line x1="22" y1="10" x2="330" y2="10"/><line x1="22" y1="30" x2="330" y2="30"/><line x1="22" y1="50" x2="330" y2="50"/><line x1="22" y1="70" x2="330" y2="70"/><line x1="22" y1="90" x2="330" y2="90"/></g>
    <g fill="#8a8f97"><text x="4" y="11">100%</text><text x="8" y="31">75%</text><text x="8" y="51">50%</text><text x="8" y="71">25%</text><text x="10" y="91">0%</text></g>
    <g fill="#e4e7eb"><rect x="40" y="10" width="12" height="84"/><rect x="72" y="10" width="12" height="84"/><rect x="104" y="10" width="12" height="84"/><rect x="136" y="10" width="12" height="84"/><rect x="168" y="10" width="12" height="84"/><rect x="200" y="10" width="12" height="84"/><rect x="232" y="10" width="12" height="84"/><rect x="264" y="10" width="12" height="84"/><rect x="296" y="10" width="12" height="84"/></g>
    <rect x="40" y="79" width="12" height="15" fill="#16498c"/><rect x="72" y="56" width="12" height="38" fill="#4a8fd8"/><rect x="104" y="62" width="12" height="32" fill="#a8c9ef"/><rect x="136" y="84" width="12" height="10" fill="#e4e7eb"/><rect x="168" y="41" width="12" height="53" fill="#16498c"/><rect x="200" y="33" width="12" height="61" fill="#4a8fd8"/><rect x="232" y="46" width="12" height="48" fill="#a8c9ef"/><rect x="264" y="64" width="12" height="30" fill="#e4e7eb"/><rect x="296" y="27" width="12" height="67" fill="#16498c"/>
    <g fill="#2b2f36" text-anchor="middle"><text x="46" y="102">2011</text><text x="78" y="102">2012</text><text x="110" y="102">2013</text><text x="142" y="102">2014</text><text x="174" y="102">2015</text><text x="206" y="102">2016</text><text x="238" y="102">2017</text><text x="270" y="102">2018</text><text x="302" y="102">2019</text></g>
  </svg>
  <footer class="foot"><span>HALVERN ENGINES | 2021</span><span>PAGE | 30</span></footer>
</section>

<!-- 31 Chart with text -->
<section class="slide">
  <h2 class="title">Chart with Text</h2>
  <div class="mark">HALVERN<br>ENGINES</div>
  <svg class="abs" style="left:20px;top:42px" width="160" height="120" viewBox="0 0 160 120" font-family="Montserrat, sans-serif" font-size="3.4">
    <text x="80" y="6" text-anchor="middle" font-size="5" fill="#2b2f36">Series 1</text>
    <g stroke="#e4e7eb" stroke-width=".5"><line x1="14" y1="16" x2="156" y2="16"/><line x1="14" y1="36" x2="156" y2="36"/><line x1="14" y1="56" x2="156" y2="56"/><line x1="14" y1="76" x2="156" y2="76"/><line x1="14" y1="96" x2="156" y2="96"/></g>
    <g fill="#16498c"><rect x="22" y="44" width="5" height="52"/><rect x="38" y="56" width="5" height="40"/><rect x="54" y="30" width="5" height="66"/><rect x="70" y="64" width="5" height="32"/><rect x="86" y="40" width="5" height="56"/><rect x="102" y="58" width="5" height="38"/><rect x="118" y="34" width="5" height="62"/><rect x="134" y="66" width="5" height="30"/></g>
    <polyline fill="none" stroke="#a8c9ef" stroke-width=".8" points="24,60 40,66 56,48 72,72 88,54 104,66 120,50 136,74"/>
    <g fill="#8a8f97" text-anchor="middle"><text x="24" y="103">2011</text><text x="56" y="103">2013</text><text x="88" y="103">2015</text><text x="120" y="103">2017</text></g>
    <rect x="40" y="110" width="6" height="2" fill="#16498c"/><text x="48" y="112" fill="#8a8f97">Series 1</text><rect x="80" y="110" width="6" height="1" fill="#a8c9ef"/><text x="88" y="112" fill="#8a8f97">2 per. Mov. Avg. (Series 1)</text>
  </svg>
  <div class="abs" style="left:210px;top:54px;width:130px">
    <div class="bar-label" style="height:8px;background:var(--navy);justify-content:flex-start;padding-left:4px;font-size:4px">Content 01</div>
    <div class="p" style="margin-top:4px">You can simply impress your audience and add a unique zing and appeal to your presentations. Easy to change colours, photos and text. Get a modern slide that is well designed. You can simply impress your audience and add a unique zing and appeal to your presentations.</div>
    <div class="p" style="margin-top:6px;text-align:center;border:.5px solid var(--grey);padding:2px;font-weight:700;color:var(--ink)">ADD YOUR TEXT HERE</div>
  </div>
  <footer class="foot"><span>HALVERN ENGINES | 2021</span><span>PAGE | 31</span></footer>
</section>

<!-- 32 Table -->
<section class="slide">
  <h2 class="title">Table Chart – Option 01</h2>
  <div class="mark">HALVERN<br>ENGINES</div>
  <div class="abs" style="left:42px;top:60px;width:10px;height:88px;display:grid;row-gap:4px">
    <span class="num" style="width:10px;height:10px;background:var(--navy);font-size:5px">●</span><span class="num" style="width:10px;height:10px;background:var(--navy);font-size:5px">▣</span><span class="num" style="width:10px;height:10px;background:var(--navy);font-size:5px">▤</span><span class="num" style="width:10px;height:10px;background:var(--navy);font-size:5px">▥</span><span class="num" style="width:10px;height:10px;background:var(--navy);font-size:5px">●</span>
  </div>
  <table class="abs" style="left:72px;top:48px;width:270px;border-collapse:collapse;font-size:3.6px;color:var(--text);text-align:center">
    <tr style="height:8px;color:#fff;font-weight:700"><td style="background:var(--navy)">TEXT HERE</td><td style="background:var(--blue)">TEXT HERE</td><td style="background:var(--navy)">TEXT HERE</td></tr>
    <tr style="height:17px;background:#f3f5f8"><td>Add Contents Title</td><td>Add Contents Title</td><td>Add Contents Title</td></tr>
    <tr style="height:17px"><td>Modern Slide</td><td>Modern Slide</td><td>Modern Slide</td></tr>
    <tr style="height:17px;background:#f3f5f8"><td>Add Contents Title</td><td>Add Contents Title</td><td>Add Contents Title</td></tr>
    <tr style="height:17px"><td>Modern Slide</td><td>Modern Slide</td><td>Modern Slide</td></tr>
    <tr style="height:17px;background:#f3f5f8"><td>Add Contents Title</td><td>Add Contents Title</td><td>Add Contents Title</td></tr>
  </table>
  <footer class="foot"><span>HALVERN ENGINES | 2021</span><span>PAGE | 32</span></footer>
</section>

<!-- 33 Structure -->
<section class="slide">
  <h2 class="title">Our Structure</h2>
  <div class="mark">HALVERN<br>ENGINES</div>
  <svg class="abs" style="left:20px;top:40px" width="140" height="140" viewBox="-70 -70 140 140" font-family="Montserrat, sans-serif" font-weight="700" font-size="7" fill="#fff">
    <g fill="none" stroke-width="18">
      <circle r="48" stroke="#16498c" stroke-dasharray="150.8 301.6" transform="rotate(90)"/>
      <circle r="48" stroke="#4a8fd8" stroke-dasharray="90.5 301.6" transform="rotate(-90)"/>
      <circle r="48" stroke="#a8c9ef" stroke-dasharray="30.2 301.6" transform="rotate(18)"/>
      <circle r="48" stroke="#d2e3f6" stroke-dasharray="30.2 301.6" transform="rotate(54)"/>
    </g>
    <text x="-60" y="2">50%</text><text x="40" y="-24">30%</text><text x="40" y="24">10%</text><text x="16" y="50">10%</text>
  </svg>
  <div class="abs" style="left:64px;top:104px;width:52px;font-size:5px;font-weight:700;color:var(--navy);text-align:center;line-height:1.1">HALVERN<br>ENGINES</div>
  <div class="abs" style="left:196px;top:42px;width:150px;display:grid;row-gap:12px;border-left:.6px solid var(--grey);padding-left:8px">
    <div class="p">✓ Get a modern slide that is well designed. Easy to change colours, photos and text.</div>
    <div class="p">✓ Get a modern slide that is well designed. Easy to change colours, photos and text.</div>
    <div class="p">✓ Get a modern slide that is well designed. Easy to change colours, photos and text.</div>
    <div class="p">✓ Get a modern slide that is well designed. Easy to change colours, photos and text.</div>
  </div>
  <footer class="foot"><span>HALVERN ENGINES | 2021</span><span>PAGE | 33</span></footer>
</section>

<!-- 34 Logos with text -->
<section class="slide">
  <h2 class="title">Logos with Text</h2>
  <div class="mark">HALVERN<br>ENGINES</div>
  <div class="abs" style="left:22px;top:58px;display:grid;grid-template-columns:repeat(3,40px);column-gap:12px;row-gap:10px">
    <div style="height:20px;background:#f3f5f8;border:.5px solid #e4e7eb"></div><div style="height:20px;background:#f3f5f8;border:.5px solid #e4e7eb"></div><div style="height:20px;background:#f3f5f8;border:.5px solid #e4e7eb"></div>
    <div style="height:20px;background:#f3f5f8;border:.5px solid #e4e7eb"></div><div style="height:20px;background:#f3f5f8;border:.5px solid #e4e7eb"></div><div style="height:20px;background:#f3f5f8;border:.5px solid #e4e7eb"></div>
    <div style="height:20px;background:#f3f5f8;border:.5px solid #e4e7eb"></div><div style="height:20px;background:#f3f5f8;border:.5px solid #e4e7eb"></div><div class="p" style="height:20px;display:flex;align-items:center;justify-content:center;text-align:center">Add Client Logo Here</div>
  </div>
  <div class="abs" style="left:196px;top:52px;width:142px;height:36px;background:#f3f5f8;padding:6px 8px"><div class="h">Contents Title</div><div class="p">Get a clean &amp; modern slide that is well designed.</div><span class="num abs" style="right:6px;top:-4px;width:12px;height:12px;background:var(--navy);font-size:4.5px">01</span></div>
  <div class="abs" style="left:196px;top:100px;width:142px;height:36px;background:#f3f5f8;padding:6px 8px"><div class="h blue">Contents Title</div><div class="p">Get a clean &amp; modern slide that is well designed.</div><span class="num abs" style="right:6px;top:-4px;width:12px;height:12px;background:var(--blue);font-size:4.5px">02</span></div>
  <footer class="foot"><span>HALVERN ENGINES | 2021</span><span>PAGE | 34</span></footer>
</section>

<!-- 35 Case study -->
<section class="slide">
  <div class="photo" role="img" aria-label="Photo of a hand signing a document" style="left:0;top:0;width:170px;height:110px;background:linear-gradient(150deg,#9aa3af,#4e5867)"></div>
  <div class="abs" style="left:0;top:110px;width:170px;height:97px;background:var(--navy)"></div>
  <div class="abs" style="left:96px;top:14px;font-size:10px;font-weight:700;color:#fff">Case Study</div>
  <div class="num abs" style="left:10px;top:102px;width:16px;height:16px;background:var(--blue);font-size:10px;font-weight:800">&rdquo;</div>
  <div class="abs" style="left:12px;top:126px;width:146px;font-size:3.6px;line-height:5.2px;color:#fff">Lorem ipsum is simply dummy text of the printing and typesetting industry. Lorem ipsum has been the standard dummy text ever since the 1500s.</div>
  <div class="abs" style="left:110px;top:160px;font-size:4px;color:#fff;font-weight:600">Name Here</div>
  <div class="mark">HALVERN<br>ENGINES</div>
  <div class="abs" style="left:194px;top:52px;width:150px;display:grid;row-gap:10px">
    <div style="display:flex;gap:6px"><span class="num" style="width:14px;height:14px;border:.6px solid var(--navy);color:var(--navy);font-size:6px;flex:none">◎</span><div><div class="h">Challenge</div><div class="p">Get a clean &amp; modern slide that is well designed. Easy to change colours, photos and text.</div></div></div>
    <div style="display:flex;gap:6px"><span class="num" style="width:14px;height:14px;border:.6px solid var(--blue);color:var(--blue);font-size:6px;flex:none">▣</span><div><div class="h blue">Solution</div><div class="p">Get a clean &amp; modern slide that is well designed. Easy to change colours, photos and text.</div></div></div>
    <div style="display:flex;gap:6px"><span class="num" style="width:14px;height:14px;border:.6px solid var(--sky);color:var(--sky);font-size:6px;flex:none">✓</span><div><div class="h" style="color:var(--sky)">Result</div><div class="p">Get a clean &amp; modern slide that is well designed. Easy to change colours, photos and text.</div></div></div>
  </div>
  <footer class="foot"><span>HALVERN ENGINES | 2021</span><span>PAGE | 35</span></footer>
</section>

<!-- 36 Disclaimer -->
<section class="slide">
  <h2 class="title">Disclaimer</h2>
  <div class="mark">HALVERN<br>ENGINES</div>
  <div class="abs" style="left:12px;right:12px;top:40px;font-size:2.7px;line-height:3.5px;color:var(--text);display:grid;row-gap:5px;text-align:justify">
    <p>This material is for information only and is not an offer to buy or sell any security or interest in any fund. Past performance is not a guide to future returns. The value of investments may fall as well as rise and investors may not get back the amount invested. Systematic strategies rely on models that may not perform as expected in all market conditions. Any forecasts, figures, opinions or techniques are for illustration only. This material is for information only and is not an offer to buy or sell any security or interest in any fund. Past performance is not a guide to future returns. The value of investments may fall as well as rise and investors may not get back the amount invested.</p>
    <p>Information herein has been obtained from sources believed to be reliable, but its accuracy is not guaranteed. It may not be reproduced or passed on without prior written consent. Systematic strategies rely on models that may not perform as expected in all market conditions. Any forecasts, figures, opinions or techniques are for illustration only. Information herein has been obtained from sources believed to be reliable, but its accuracy is not guaranteed. It may not be reproduced or passed on without prior written consent. This material is for information only and is not an offer to buy or sell any security or interest in any fund.</p>
    <p>Issued for professional investors only. Not for retail distribution. Trading in leveraged and derivative products carries a high level of risk. Figures are shown gross of fees unless stated otherwise. Issued for professional investors only. Not for retail distribution. Trading in leveraged and derivative products carries a high level of risk and may not suit all investors.</p>
  </div>
  <footer class="foot"><span>HALVERN ENGINES | 2021</span><span>PAGE | 36</span></footer>
</section>

<!-- 37 Icons -->
<section class="slide">
  <h2 class="title">Free Icons</h2>
  <div class="mark">HALVERN<br>ENGINES</div>
  <div class="art" role="img" aria-label="Grid of grey outline business icons" style="left:12px;right:12px;top:40px;height:150px;background:repeating-linear-gradient(90deg,#d7dbe0 0 8px,transparent 8px 13px),repeating-linear-gradient(0deg,#fff 0 5px,transparent 5px 13px);opacity:.7"></div>
  <footer class="foot"><span>HALVERN ENGINES | 2021</span><span>PAGE | 37</span></footer>
</section>

<!-- 38 Thank you dark -->
<section class="slide dark">
  <div class="art" role="img" aria-label="Faint blue network texture" style="inset:0;background:linear-gradient(135deg,var(--navy),#1b528f 60%,var(--navy-deep))"></div>
  <div class="abs" style="left:28px;top:30px;font-size:11px;font-weight:700;color:var(--sky);letter-spacing:.5px">THANK YOU</div>
  <div class="abs" style="left:28px;top:66px;font-size:4.4px;font-weight:700;color:#fff;letter-spacing:.6px">PRESENTER NAME</div>
  <div class="abs" style="left:28px;top:82px;display:grid;row-gap:7px;font-size:3.8px;color:#fff">
    <div>☎&nbsp;&nbsp; +1 234 567 890</div><div>◍&nbsp;&nbsp; www.yourwebsite.com</div><div>✉&nbsp;&nbsp; addyouremail@here.com</div><div>⚲&nbsp;&nbsp; Add your location here</div>
  </div>
  <div class="logo white abs" style="left:184px;width:170px;top:88px;font-size:12px">HALVERN<br>ENGINES</div>
  <div class="abs" style="left:0;right:0;bottom:6px;text-align:center;font-size:2.8px;color:var(--sky)">Get a clean &amp; modern slide that is well designed.</div>
</section>

<!-- 39 Thank you light -->
<section class="slide">
  <div class="art" role="img" aria-label="Faint grey network of connected nodes" style="inset:0;background:radial-gradient(ellipse at 70% 50%,#fff 30%,#eef0f3 80%)"></div>
  <div class="abs" style="left:28px;top:30px;font-size:11px;font-weight:700;color:var(--blue);letter-spacing:.5px">THANK YOU</div>
  <div class="abs" style="left:28px;top:66px;font-size:4.4px;font-weight:700;color:var(--ink);letter-spacing:.6px">PRESENTER NAME</div>
  <div class="abs" style="left:28px;top:82px;display:grid;row-gap:7px;font-size:3.8px;color:var(--ink)">
    <div><span style="color:var(--navy)">☎</span>&nbsp;&nbsp; +1 234 567 890</div><div><span style="color:var(--navy)">◍</span>&nbsp;&nbsp; www.yourwebsite.com</div><div><span style="color:var(--navy)">✉</span>&nbsp;&nbsp; addyouremail@here.com</div><div><span style="color:var(--navy)">⚲</span>&nbsp;&nbsp; Add your location here</div>
  </div>
  <div class="logo abs" style="left:184px;width:170px;top:88px;font-size:12px;color:var(--ink)">HALVERN<br>ENGINES</div>
  <div class="abs" style="left:0;right:0;bottom:6px;text-align:center;font-size:2.8px;color:var(--grey-dark)">Get a clean &amp; modern slide that is well designed.</div>
</section>

</main>
</body>
</html>
```